Business card design based on existing website

Please make a business card that is consistent with the look and feel of my new website: http://tellbury.com.sg. By going to the site, I think you'll have all you need in terms of the work I do and the colors I use.

I would like to ask the winner of this project to then do a separate project to design my stationery.

Target Market(s)

Heads of human resources, people wanting psychotherapy, and executives wanting coaching. (It's quite a mix!)

Industry/Entity Type

Psychology

Contact Information for Business Card

Email: ray5678@tellbury.com.sg
Website: http://tellbury.com.sg
Tel: +65 94706218

(I will not have a physical address on the card)

Font styles to use
Serif

Colors

Designer to choose colors to be used in the design.

Requirements
Must have
• On the Front
• ==========
• Have "Dr. Raymond Tellbury" using the font of the website.
• Also "Executive Coach, Psychotherapist, Leadership Professor"
• The back should mention
• ==================
• My degrees
• -------------
• "PhD Kelworth; Post Doc Drayfield". E.g., "Raymond Tellbury (PhD Kelworth; Post Doc Drayfield)" where the text between brackets was in smaller font.
• My work
• ----------
• "Executive coach, psychotherapist, and leadership professor"
• My job titles
• ---------------
• "Principal (Tellbury Consulting)
• Adjunct Professor (Lornvale Commerce University)
• Adjunct Associate Professor (Pemberly Institute of Letters)
• Coach & Supervisor (OKTRAV) '
• Options:
• 1) you can abbreviate Adjunct Professor to "Adj Prof" or "Adj Professor"; and "Adjunct Associate Professor" to "Adj Assoc Prof"
• 2) you abbreviate "Pemberly Institute of Letters" and "Lornvale Commerce University" to "PIL" and "LCU"
• 3) You can also combine the titles for PIL and LCU, e.g., "Adjunct faculty (PIL & LCU)
Nice to have
• Because I work with many Chinese people, it is sometimes helpful to have my family name, "Tellbury", in caps. In the past I have not used caps because it takes away from the aesthetic of the card. Only use caps if it looks good.
• The uploaded image of a "RT" is something that may be helpful. I am undecided.
• THANK YOU for helping me!
Should not have
• No photos. In my industry people consider it overselling.

```html
<!DOCTYPE html>
<html lang="en">
<head>
<meta charset="utf-8">
<title>Raymond Tellbury – Business Card</title>
<link href="https://fonts.googleapis.com/css2?family=Lato:wght@400;700&family=Pinyon+Script&display=swap" rel="stylesheet">
<style>
  :root {
    --stage: #e6e4e1;
    --card-cream: #ebe2d5;
    --ink: #1c1c1c;
    --ink-soft: #4a4540;
    --rule: #b9ad9c;
    --forest-text: #2f5228;
    --forest-dark: #0f1a10;
    --forest-mid: #1f3a1f;
    --forest-light: #2f5228;
    --lime: #c6ef2b;
    --white: #ffffff;
  }
  * { margin: 0; padding: 0; box-sizing: border-box; }
  html, body {
    width: 1200px; height: 900px; overflow: hidden;
    background: var(--stage);
  }
  .canvas { position: relative; width: 1200px; height: 900px; }

  .card { position: absolute; overflow: hidden; box-shadow: 0 6px 18px rgba(0,0,0,.18); }

  /* Front */
  .card-front {
    left: 78px; top: 35px; width: 587px; height: 363px;
    background: var(--card-cream);
    font-family: "Lato", sans-serif; color: var(--ink);
  }
  .name {
    position: absolute; left: 27px; top: 191px;
    font-size: 21px; font-weight: 700; letter-spacing: .3px;
  }
  .credentials { position: absolute; left: 31px; top: 219px; font-size: 16px; }
  .contact-list { position: absolute; left: 32px; top: 256px; list-style: none; font-size: 16px; }
  .contact-list li { display: flex; align-items: center; height: 22px; }
  .contact-list svg { width: 13px; height: 13px; margin-right: 6px; fill: var(--ink); }

  .column-rule {
    position: absolute; left: 318px; top: 186px; width: 1px; height: 138px;
    background: var(--rule);
  }
  .practice {
    position: absolute; left: 336px; top: 183px; width: 225px;
    font-size: 14px; line-height: 19px; font-weight: 700; color: var(--forest-text);
  }
  .appointments {
    position: absolute; left: 336px; top: 232px; width: 225px;
    list-style: none; font-size: 14px; line-height: 23px; color: var(--ink-soft);
  }

  /* Back */
  .card-back {
    left: 388px; top: 505px; width: 567px; height: 352px;
    font-family: "Lato", sans-serif;
  }
  .foliage-area {
    position: absolute; inset: 0;
    background:
      radial-gradient(ellipse at 85% 20%, var(--forest-light) 0%, transparent 45%),
      radial-gradient(ellipse at 30% 55%, var(--forest-mid) 0%, transparent 55%),
      linear-gradient(180deg, #142414 0%, var(--forest-dark) 100%);
  }
  .tagline {
    position: absolute; left: 0; right: 0; top: 92px;
    text-align: center; color: var(--lime); font-weight: 400;
    font-family: "Pinyon Script", cursive; font-size: 50px; line-height: 66px;
  }
  .divider {
    position: absolute; left: 92px; top: 236px; width: 305px; height: 1px;
    background: var(--lime); opacity: .5;
  }
  .services {
    position: absolute; left: 0; right: 0; top: 272px;
    display: flex; justify-content: center; align-items: center;
    color: var(--white); font-size: 16.5px;
  }
  .services .dot {
    width: 8px; height: 8px; border-radius: 50%;
    background: var(--lime); margin: 0 16px;
  }
</style>
</head>
<body>
<div class="canvas">

  <section class="card card-front">
    <h1 class="name">DR. RAYMOND TELLBURY</h1>
    <p class="credentials">PhD Kelworth, Post Doc Drayfield</p>
    <ul class="contact-list">
      <li>
        <svg viewBox="0 0 16 16" aria-hidden="true"><path d="M1 5c0-2 3-3 7-3s7 1 7 3v1h-4V5H5v1H1zM4 7h8l2 7H2zm4 1.5a2.5 2.5 0 1 0 0 5 2.5 2.5 0 0 0 0-5z"/></svg>
        +65 94706218
      </li>
      <li>
        <svg viewBox="0 0 16 16" aria-hidden="true"><path d="M1 3h14v10H1zm1.5 1.5v.4L8 9l5.5-4.1v-.4zM2.5 6.6v5h11v-5L8 10.7z"/></svg>
        ray5678@tellbury.com.sg
      </li>
      <li>
        <svg viewBox="0 0 16 16" aria-hidden="true"><circle cx="8" cy="8" r="7"/><path d="M5 4c1 1 3 1 3 3s-2 1-2 3 1 2 1 3M10 3c0 2 2 2 3 3M10 13c0-2 1-3 3-3" stroke="#ebe2d5" stroke-width="1.3" fill="none"/></svg>
        www.tellbury.com.sg
      </li>
    </ul>

    <div class="column-rule"></div>
    <p class="practice">Executive Coach, Psychotherapist,<br>Leadership Professor</p>
    <ul class="appointments">
      <li>Principal (Tellbury Consulting)</li>
      <li>Adj Professor (LCU)</li>
      <li>Adj Assoc Prof (PIL)</li>
      <li>Coach &amp; Supervisor (OKTRAV)</li>
    </ul>
  </section>

  <section class="card card-back">
    <div class="foliage-area" role="img" aria-label="Dark green forest foliage background"></div>
    <h2 class="tagline">Advancing Human<br>Development</h2>
    <div class="divider"></div>
    <p class="services">
      <span>Executive coaching</span><span class="dot"></span>
      <span>Psychotherapy</span><span class="dot"></span>
      <span>Leadership Training</span>
    </p>
  </section>

</div>
</body>
</html>
```